Mezzanine Floor Manufacturer looking for a new business card design

We manufacture mezzanine floors and are providers of racking systems. We provide a range of items/services - simple rack repairs , full warehouse fit outs , manufacturer and install mezzanine floors , partitioning and large turnkey projects. Recently had a new website - www.corvane-shelving.co.uk and would like our business cards updating aswell . Our current card is single sided in the old logo colours (pdf attached) and needs updating.

Target Market(s)

We deal with large projects/ multi national companies and also smaller projects and companies throughout the UK ranging from a single warehouse to a large multi site company.

Industry/Entity Type

Business

Contact Information for Business Card

Will have job title,tel no's, email ,website address etc like example pdf

Requirements
Must have
• Hi - needs to use the colours of the logo & new website. Card needs to be professional

```html
<!DOCTYPE html>
<html lang="en">
<head>
<meta charset="utf-8">
<title>Corvane Shelving – Business Card</title>
<link href="https://fonts.googleapis.com/css2?family=Lato:wght@400;700&display=swap" rel="stylesheet">
<style>
  :root {
    --backdrop: #dcdcdc;
    --brand-red: #dd2a1b;
    --deep-red: #c81d12;
    --paper: #ffffff;
    --silver-light: #f1f1f1;
    --silver-dark: #9a9a9a;
    --ink-light: #ffffff;
    --ink-muted: #f5c9c4;
  }
  * { box-sizing: border-box; margin: 0; padding: 0; }
  html, body { width: 1200px; height: 675px; overflow: hidden; }
  body {
    background: var(--backdrop);
    font-family: "Lato", sans-serif;
    position: relative;
  }
  .card {
    position: absolute;
    top: 194px;
    width: 500px;
    height: 286px;
    overflow: hidden;
    box-shadow: 0 10px 24px rgba(0,0,0,0.18);
  }
  .card-front { left: 66px; background: var(--brand-red); }
  .card-back { left: 634px; background: var(--brand-red); }
  .card-art { position: absolute; inset: 0; width: 100%; height: 100%; }

  .brand-mark {
    position: absolute;
    left: 0; right: 0;
    display: flex;
    align-items: center;
    justify-content: center;
    gap: 10px;
    color: var(--ink-light);
    font-weight: 700;
  }
  .brand-mark .brand-dot {
    width: 16px; height: 16px; border-radius: 50%;
    background: var(--ink-light);
  }
  .card-front .brand-mark { top: 92px; font-size: 48px; letter-spacing: 1px; }
  .front-url {
    position: absolute;
    top: 186px; left: 0; right: 0;
    text-align: center;
    color: var(--ink-light);
    font-size: 15px;
    letter-spacing: 2.5px;
  }

  .card-back .brand-mark {
    top: 62px; left: 325px; right: 14px;
    font-size: 30px; gap: 7px;
  }
  .card-back .brand-mark .brand-dot { width: 11px; height: 11px; }

  .contact {
    position: absolute;
    left: 36px; top: 108px;
    color: var(--ink-light);
  }
  .contact-name { font-size: 17px; font-weight: 700; }
  .contact-role { font-size: 12px; color: var(--ink-muted); margin-bottom: 12px; }
  .contact-address { font-size: 13px; line-height: 1.3; margin-bottom: 12px; }
  .contact-list { list-style: none; font-size: 13px; line-height: 1.45; }
  .contact-list li { display: flex; align-items: center; gap: 8px; }
  .contact-list svg { width: 12px; height: 12px; flex: none; }
</style>
</head>
<body>

<section class="card card-front" aria-label="Card front">
  <svg class="card-art" viewBox="0 0 500 286" preserveAspectRatio="none" aria-hidden="true">
    <defs>
      <linearGradient id="silver-edge" x1="0" y1="0" x2="1" y2="0">
        <stop offset="0" stop-color="var(--silver-dark)"/>
        <stop offset="0.5" stop-color="var(--silver-light)"/>
        <stop offset="1" stop-color="var(--silver-dark)"/>
      </linearGradient>
    </defs>
    <path d="M0,0 L14,0 C30,80 0,160 16,286 L0,286 Z" fill="url(#silver-edge)"/>
    <path d="M500,0 L486,0 C470,90 500,170 484,286 L500,286 Z" fill="url(#silver-edge)"/>
  </svg>
  <div class="brand-mark"><span class="brand-dot"></span><span>Corvane</span></div>
  <p class="front-url">www.corvane-shelving.co.uk</p>
</section>

<section class="card card-back" aria-label="Card back">
  <svg class="card-art" viewBox="0 0 500 286" preserveAspectRatio="none" aria-hidden="true">
    <defs>
      <linearGradient id="silver-band" x1="0" y1="0" x2="1" y2="1">
        <stop offset="0" stop-color="var(--silver-dark)"/>
        <stop offset="0.5" stop-color="var(--silver-light)"/>
        <stop offset="1" stop-color="var(--silver-dark)"/>
      </linearGradient>
    </defs>
    <path d="M258,0 C262,130 360,214 500,228 L500,0 Z" fill="url(#silver-band)"/>
    <path d="M276,0 C282,122 372,204 500,218 L500,0 Z" fill="var(--deep-red)"/>
    <path d="M290,0 C298,118 384,196 500,206 L500,0 Z" fill="var(--paper)"/>
  </svg>

  <div class="brand-mark"><span class="brand-dot" style="background:var(--brand-red)"></span><span style="color:var(--brand-red)">Corvane</span></div>

  <div class="contact">
    <p class="contact-name">Mara Ellison</p>
    <p class="contact-role">Manager</p>
    <p class="contact-address">4100 Hale Row<br>Denford TX 78010</p>
    <ul class="contact-list">
      <li><svg viewBox="0 0 12 12" aria-hidden="true"><path d="M2.5 1 L4.5 1 L5.5 3.5 L4.2 4.5 C4.8 6 6 7.2 7.5 7.8 L8.5 6.5 L11 7.5 L11 9.5 C11 10.3 10.3 11 9.5 11 C5 11 1 7 1 2.5 C1 1.7 1.7 1 2.5 1 Z" fill="var(--ink-light)"/></svg>512 004 2290</li>
      <li><svg viewBox="0 0 12 12" aria-hidden="true"><rect x="3" y="1" width="6" height="4" fill="none" stroke="var(--ink-light)"/><rect x="1" y="5" width="10" height="5" fill="var(--ink-light)"/></svg>512 004 2291</li>
      <li><svg viewBox="0 0 12 12" aria-hidden="true"><rect x="1" y="2.5" width="10" height="7" fill="none" stroke="var(--ink-light)"/><path d="M1 2.5 L6 7 L11 2.5" fill="none" stroke="var(--ink-light)"/></svg>info@marafinance.com</li>
      <li><svg viewBox="0 0 12 12" aria-hidden="true"><circle cx="6" cy="6" r="5" fill="none" stroke="var(--ink-light)"/><ellipse cx="6" cy="6" rx="2" ry="5" fill="none" stroke="var(--ink-light)"/><path d="M1 6 H11" stroke="var(--ink-light)"/></svg>www.marafinance.com</li>
    </ul>
  </div>
</section>

</body>
</html>
```